Letterhead Design Project

We have recently updated our corporate logo and are seeking a new letterhead template.

Attached is the new logo and the old letterhead.

PLEASE DO NOT USE OUR EXISTING WEB SITE FOR INSPIRATION as we are redesigning it.

Target Market(s)

Executives, search professionals, technical and scientific professionals

Industry/Entity Type

Seeking

```html
<!DOCTYPE html>
<html lang="en">
<head>
<meta charset="utf-8">
<title>HelixSeek Letterhead</title>
<link rel="stylesheet" href="https://fonts.googleapis.com/css2?family=Source+Sans+3:wght@400;700&display=swap">
<style>
  :root {
    --brand-blue: #1591ce;
    --ink: #2b2b2b;
    --decor-grey: #ebebeb;
    --paper: #ffffff;
  }
  * { margin: 0; padding: 0; box-sizing: border-box; }
  html, body { width: 927px; height: 1200px; overflow: hidden; background: var(--paper); }
  .letterhead {
    position: relative;
    width: 927px;
    height: 1200px;
    background: var(--paper);
    font-family: "Source Sans 3", "Myriad Pro", Arial, sans-serif;
    overflow: hidden;
  }
  .brand {
    position: absolute;
    left: 27px;
    top: 30px;
    display: flex;
    align-items: center;
    gap: 10px;
  }
  .brand-dot {
    width: 56px;
    height: 56px;
    border-radius: 50%;
    background: var(--brand-blue);
  }
  .brand-name {
    font-size: 46px;
    font-weight: 700;
    color: var(--brand-blue);
    letter-spacing: -0.5px;
    line-height: 1;
  }
  .contact {
    position: absolute;
    right: 35px;
    top: 46px;
    width: 380px;
    text-align: center;
    font-size: 14.5px;
    line-height: 19px;
    color: var(--ink);
  }
  .contact .sep { color: var(--brand-blue); margin: 0 4px; }
  .decor-mark {
    position: absolute;
    left: 0;
    top: 650px;
    width: 280px;
    height: 440px;
  }
  .footer-band {
    position: absolute;
    left: 0;
    top: 1159px;
    width: 927px;
    height: 18px;
  }
  .band-left, .band-right {
    position: absolute;
    top: 0;
    height: 18px;
    background: var(--brand-blue);
  }
  .band-left { left: 0; width: 575px; border-radius: 0 9px 9px 0; }
  .band-right { left: 778px; width: 149px; border-radius: 9px 0 0 9px; }
  .web-address {
    position: absolute;
    left: 583px;
    top: -3px;
    width: 188px;
    text-align: center;
    font-size: 17px;
    line-height: 24px;
    color: var(--brand-blue);
  }
</style>
</head>
<body>
  <div class="letterhead">
    <header>
      <div class="brand">
        <span class="brand-dot"></span>
        <span class="brand-name">HelixSeek</span>
      </div>
      <address class="contact" style="font-style: normal;">
        2400 Lakeview Road, Suite 140<span class="sep">•</span>Ashford, MA 01720<br>
        Phone 555.201.0100<span class="sep">•</span>Fax 555.201.0110
      </address>
    </header>

    <svg class="decor-mark" viewBox="0 0 280 440" aria-hidden="true">
      <circle cx="55" cy="220" r="215" fill="var(--decor-grey)"/>
    </svg>

    <footer class="footer-band">
      <span class="band-left"></span>
      <span class="web-address">www.helixseek.com</span>
      <span class="band-right"></span>
    </footer>
  </div>
</body>
</html>
```